Brisk Wire Services - Electrical

We need flyers for electrical services.
Areas of work include new builds, office fitouts, switchboard upgrades, installation of ceiling fans, powerpoint and downlight upgrades, home theatre and AV systems, all exterior and emergency work. Free quotes
We would like to see designs with the colour Red with a young and modern design. Licence No: 83146K must be included and call Leopold on 0418693027.

Colors
ec1f27

```html
<!DOCTYPE html>
<html lang="en">
<head>
<meta charset="utf-8">
<title>Brisk Wire Services – Electrical Flyer</title>
<link rel="stylesheet" href="https://fonts.googleapis.com/css2?family=Exo+2:ital,wght@1,800;1,900&family=Lato:ital,wght@0,400;0,700;1,400&display=swap">
<style>
  :root {
    --red: #ec1f27;
    --red-soft: #f4a0a4;
    --blue: #2a7fd4;
    --blue-deep: #3257b0;
    --navy: #2e4aa8;
    --white: #ffffff;
    --ink: #2b2b2b;
    --ring: #d6d6d6;
    --photo-light: #e6e6e6;
    --photo-dark: #6b737d;
    --backdrop: #3c3c3c;
  }
  * { margin: 0; padding: 0; box-sizing: border-box; }
  html, body {
    width: 1200px; height: 1200px; overflow: hidden;
    background: var(--backdrop);
  }
  .canvas {
    position: relative; width: 1200px; height: 1200px;
  }
  .flyer {
    position: absolute; left: 204px; top: 40px;
    width: 792px; height: 1120px;
    display: block;
  }
  .display { font-family: "Exo 2", "Arial Black", sans-serif; font-style: italic; font-weight: 900; }
  .body { font-family: "Lato", Arial, sans-serif; }
  .feature { font-family: "Lato", Arial, sans-serif; font-weight: 700; font-size: 22px; fill: var(--navy); }
  .service { font-family: "Lato", Arial, sans-serif; font-weight: 700; font-size: 23px; fill: var(--white); }
</style>
</head>
<body>
<div class="canvas">
<svg class="flyer" viewBox="0 0 872 1235" xmlns="http://www.w3.org/2000/svg">
  <defs>
    <linearGradient id="quoteBar" x1="0" x2="1" y1="0" y2="0">
      <stop offset="0" stop-color="var(--red)"/>
      <stop offset="0.55" stop-color="var(--red)" stop-opacity="0.85"/>
      <stop offset="1" stop-color="var(--red-soft)" stop-opacity="0.15"/>
    </linearGradient>
    <linearGradient id="photoTone" x1="0" x2="1" y1="0" y2="0">
      <stop offset="0" stop-color="var(--photo-dark)"/>
      <stop offset="0.45" stop-color="#b9bcc0"/>
      <stop offset="1" stop-color="var(--photo-light)"/>
    </linearGradient>
    <linearGradient id="servicesTone" x1="0" x2="0" y1="0" y2="1">
      <stop offset="0" stop-color="var(--blue)"/>
      <stop offset="1" stop-color="var(--blue-deep)"/>
    </linearGradient>
    <linearGradient id="pill" x1="0" x2="1" y1="0" y2="0">
      <stop offset="0" stop-color="#ffffff" stop-opacity="0"/>
      <stop offset="0.35" stop-color="#ffffff" stop-opacity="0.9"/>
      <stop offset="1" stop-color="#ffffff"/>
    </linearGradient>
  </defs>

  <!-- page -->
  <rect class="sheet" width="872" height="1235" fill="var(--white)"/>

  <!-- hero photo area -->
  <rect class="hero-photo" x="0" y="212" width="760" height="455" fill="url(#photoTone)"
        role="img" aria-label="Photo of an electrician in a hard hat and glasses stripping wires at a wall outlet"/>

  <!-- red headline panel -->
  <path class="headline-panel" d="M701,0 L872,0 L872,832 L720,650 L440,292 Q418,258 446,226 Z" fill="var(--red)"/>

  <!-- free quotes bar -->
  <rect class="quote-bar" x="161" y="43" width="540" height="107" fill="url(#quoteBar)"/>
  <text class="display" x="205" y="112" font-size="34" fill="var(--white)">FREE QUOTES!</text>

  <!-- company mark -->
  <circle class="logo-ring" cx="112" cy="101" r="70" fill="var(--white)" stroke="var(--ring)" stroke-width="5"/>
  <text class="body" x="112" y="86" font-size="17" font-weight="700" fill="var(--ink)" text-anchor="middle">
    <tspan x="112">BRISK</tspan><tspan x="112" dy="21">WIRE</tspan><tspan x="112" dy="21">SERVICES</tspan>
  </text>

  <!-- headline -->
  <text class="display" x="854" y="205" font-size="52" fill="var(--white)" text-anchor="end">NEED</text>
  <text class="display" x="854" y="246" font-size="34" fill="var(--white)" text-anchor="end">AN ELECTRICIAN?</text>
  <rect x="495" y="258" width="377" height="4" fill="var(--white)"/>
  <text class="body" x="856" y="297" font-size="19" fill="var(--white)" text-anchor="end">LICENSE NO: 83146K</text>
  <text class="body" x="856" y="345" font-size="19" fill="var(--white)" text-anchor="end">
    <tspan x="856">Your Company Short Introduction</tspan>
    <tspan x="856" dy="25">Here or Company Slogan</tspan>
  </text>

  <!-- feature pills -->
  <g class="features">
    <rect x="270" y="452" width="300" height="48" fill="url(#pill)"/>
    <text class="feature" x="520" y="485" text-anchor="end">LOCALLY OWNED</text>
    <circle cx="571" cy="475" r="35" fill="var(--navy)" stroke="#f5c2c4" stroke-width="5"/>
    <path d="M556,478 L571,464 L586,478 M560,476 L560,490 L582,490 L582,476" fill="none" stroke="var(--white)" stroke-width="3.5" stroke-linejoin="round"/>

    <rect x="330" y="535" width="310" height="50" fill="url(#pill)"/>
    <text class="feature" x="592" y="569" text-anchor="end">CUSTOMER FOCUSED</text>
    <circle cx="641" cy="560" r="35" fill="var(--navy)" stroke="#f5c2c4" stroke-width="5"/>
    <circle cx="641" cy="551" r="6" fill="var(--white)"/>
    <circle cx="628" cy="555" r="5" fill="var(--white)"/>
    <circle cx="654" cy="555" r="5" fill="var(--white)"/>
    <path d="M629,575 Q629,561 641,561 Q653,561 653,575 Z M619,572 Q619,562 628,562 Q632,562 634,564 Q628,568 627,572 Z M663,572 Q663,562 654,562 Q650,562 648,564 Q654,568 655,572 Z" fill="var(--white)"/>

    <rect x="400" y="612" width="312" height="48" fill="url(#pill)"/>
    <text class="feature" x="660" y="646" text-anchor="end">QUALIFIED TEAM</text>
    <circle cx="713" cy="634" r="35" fill="var(--navy)" stroke="#f5c2c4" stroke-width="5"/>
    <path d="M713,616 L718,628 L731,629 L721,637 L724,650 L713,643 L702,650 L705,637 L695,629 L708,628 Z" fill="none" stroke="var(--white)" stroke-width="2.5" stroke-linejoin="round"/>
  </g>

  <!-- services panel -->
  <path class="services-panel" d="M0,667 L735,667 L872,832 L872,1180 L560,1180 L490,1112 L0,1112 Z" fill="url(#servicesTone)"/>
  <text class="display" x="38" y="721" font-size="36" fill="var(--white)">OUR SERVICES</text>
  <path d="M0,736 L530,736 Q545,736 545,748 Q545,758 556,752 L570,738" fill="none" stroke="var(--white)" stroke-width="4"/>
  <path d="M570,727 L585,727 L585,757 L570,757 Z M585,733 L612,733 M585,751 L612,751" fill="none" stroke="var(--white)" stroke-width="4"/>
  <text class="body" x="38" y="763" font-size="19" font-style="italic" fill="var(--white)">INCLUDE BUT NOT LIMITED TO:</text>

  <g class="service-list">
    <g fill="none" stroke="var(--white)" stroke-width="3.5" stroke-linecap="round" stroke-linejoin="round">
      <path d="M96,800 L103,808 L117,788"/>
      <path d="M96,835 L103,843 L117,823"/>
      <path d="M96,870 L103,878 L117,858"/>
      <path d="M96,905 L103,913 L117,893"/>
      <path d="M96,940 L103,948 L117,928"/>
      <path d="M96,975 L103,983 L117,963"/>
      <path d="M96,1010 L103,1018 L117,998"/>
      <path d="M96,1045 L103,1053 L117,1033"/>
      <path d="M96,1080 L103,1088 L117,1068"/>
    </g>
    <text class="service" x="130" y="808">NEW BUILDS</text>
    <text class="service" x="130" y="843">OFFICE FITOUTS</text>
    <text class="service" x="130" y="878">SWITCHBOARD UPGRADES</text>
    <text class="service" x="130" y="913">INSTALLATION OF CEILING FANS</text>
    <text class="service" x="130" y="948">POWERPOINT</text>
    <text class="service" x="130" y="983">DOWNLIGHT UPGRADES</text>
    <text class="service" x="130" y="1018">HOME THEATRE &amp; AV SYSTEMS</text>
    <text class="service" x="130" y="1053">EXTERIOR WORK</text>
    <text class="service" x="130" y="1088">EMERGENCY WORKS</text>
  </g>

  <!-- contact band -->
  <path class="contact-band" d="M0,1130 L501,1130 L601,1235 L0,1235 Z" fill="var(--red)"/>
  <text class="display" x="90" y="1180" font-size="34" fill="var(--white)">CONTACT</text>
  <path d="M64,1196 Q62,1200 66,1206 Q71,1213 76,1212 L78,1208 L74,1205 L71,1207 Q68,1204 67,1201 L69,1199 L67,1195 Z" fill="var(--white)"/>
  <text class="body" x="93" y="1208" font-size="22" font-weight="700" fill="var(--white)">0418693027 (Leopold)</text>

  <!-- social placeholders -->
  <circle cx="688" cy="1174" r="33" fill="var(--red)" stroke="#f5c2c4" stroke-width="5"/>
  <circle cx="775" cy="1174" r="33" fill="var(--red)" stroke="#f5c2c4" stroke-width="5"/>
</svg>
</div>
</body>
</html>
```